KGDB Business Card

Looking for a business card design to incorporate our branding. We want to only use the colors listing in the Branding Package (attached).
Updates

Target Market(s)

People who need their phone or device fixed.

Industry/Entity Type

Electronics

Contact Information for Business Card

Please use:

Bright Circuit Mending Depot LLC
3478 S Ridge Trail 2210 E
Suite 417
San Antonio, TX 78341

Marcus Delwyn, Store Manager

(210) 555-0143

Requirements
Must have
• Must include the colors that are contained within the Branding Package PDF file.

```html
<!DOCTYPE html>
<html lang="en">
<head>
<meta charset="utf-8">
<title>KGDB Business Card</title>
<link rel="stylesheet" href="https://fonts.googleapis.com/css2?family=Questrial&display=swap">
<style>
  :root {
    --orange: #e8672a;
    --orange-light: #f07a35;
    --orange-deep: #d85420;
    --grey: #77787b;
    --white: #ffffff;
    --paper: #f6f6f4;
    --backdrop: #e9e6e1;
  }
  * { box-sizing: border-box; margin: 0; padding: 0; }
  html, body { width: 1200px; height: 780px; overflow: hidden; }
  body {
    background: var(--backdrop);
    font-family: "Questrial", sans-serif;
    position: relative;
  }
  .card {
    position: absolute;
    top: 247px;
    width: 500px;
    height: 286px;
    border-radius: 4px;
    overflow: hidden;
    box-shadow: 0 6px 18px rgba(0,0,0,0.18);
  }
  /* Front */
  .card-front { left: 70px; background: var(--paper); }
  .brand {
    position: absolute; left: 34px; top: 78px;
    display: flex; align-items: center; gap: 12px;
  }
  .brand-square {
    width: 44px; height: 44px; border-radius: 10px;
    background: var(--orange);
  }
  .brand-name {
    color: var(--orange);
    font-size: 25px;
    line-height: 1.05;
    width: 260px;
  }
  .corner-panel {
    position: absolute; right: 0; top: 0;
    width: 140px; height: 152px;
    background: linear-gradient(160deg, var(--orange-light), var(--orange-deep));
    border-bottom-left-radius: 26px;
  }
  .name-band {
    position: absolute; left: 0; top: 160px;
    width: 352px; height: 28px;
    background: var(--grey);
    color: var(--white);
    font-size: 14px;
    display: flex; align-items: center;
    padding-left: 34px;
  }
  .name-band .divider { margin: 0 8px; }
  .name-band .role { font-size: 12px; }
  .contact-panel {
    position: absolute; left: 0; right: 0; bottom: 0; top: 188px;
    background: linear-gradient(90deg, var(--orange-deep), var(--orange-light));
    color: var(--white);
    padding: 9px 34px 0;
  }
  .contact-side {
    position: absolute; left: 360px; right: 0; top: 160px; height: 28px;
    background: var(--orange-deep);
    border-top-left-radius: 14px;
  }
  .company { font-size: 15px; margin-bottom: 4px; }
  .address { font-size: 12px; line-height: 1.35; }
  .phone { font-size: 12px; display: flex; align-items: center; gap: 6px; margin-top: 4px; }
  .phone svg { width: 14px; height: 14px; }
  /* Back */
  .card-back {
    left: 630px;
    background: linear-gradient(150deg, var(--orange-light), var(--orange-deep));
  }
  .back-texture {
    position: absolute; inset: 0;
    background: radial-gradient(ellipse at 40% 30%, rgba(255,255,255,0.06), rgba(0,0,0,0.05));
  }
  .back-brand {
    position: absolute; inset: 0;
    display: flex; flex-direction: column; align-items: center; justify-content: center; gap: 18px;
  }
  .back-square {
    width: 82px; height: 82px; border-radius: 18px;
    border: 3px solid var(--white);
  }
  .back-name { color: var(--white); font-size: 17px; letter-spacing: 0.3px; }
</style>
</head>
<body>
  <section class="card card-front">
    <div class="brand">
      <div class="brand-square"></div>
      <div class="brand-name">Bright Circuit Mending Depot</div>
    </div>
    <div class="corner-panel"></div>
    <div class="name-band">
      <span class="person">Marcus Delwyn</span><span class="divider">|</span><span class="role">Store Manager</span>
    </div>
    <div class="contact-side"></div>
    <div class="contact-panel">
      <p class="company">Bright Circuit Mending Depot LLC</p>
      <p class="address">3478 S Ridge Trail 2210 E<br>Suite 417, San Antonio, TX 78341</p>
      <p class="phone">
        <svg viewBox="0 0 14 14" aria-hidden="true"><rect width="14" height="14" rx="3" fill="#fff"/><path d="M4.2 3.2l1.5 0 .6 1.9-.9.7c.5 1.1 1.3 1.9 2.4 2.4l.7-.9 1.9.6 0 1.5c-3.6.2-6.4-2.6-6.2-6.2z" fill="#e8672a"/></svg>
        (210) 555-0143
      </p>
    </div>
  </section>

  <section class="card card-back">
    <div class="back-texture" role="img" aria-label="Faint repeating brand pattern across the orange background"></div>
    <div class="back-brand">
      <div class="back-square"></div>
      <p class="back-name">Bright Circuit Mending Depot LLC</p>
    </div>
  </section>
</body>
</html>
```